New company that wants to specialize in presale property and garden do ups

I own A landscaping and premium garden maintenance company.
I want to advertise to people that are listing there homes for sale.
For the purpose of using my company services to fix up there home and gardens to maximize there sale potential. I am on instagram as trvbloom_landscaping. I am aiming for the higher end of the market. This Flyer will be post card size. I would like my logo to be used. And your layout to be clean cut and easy to read. I need my clients to understand that spending time on there gardens appearance will aid with sale of there home and maximize there profit
Target Market(s)
People selling there homes. or thinking about selling there homes
Industry/Entity Type
Landscape Gardening
Requirements
Must have
- Email address neil@trvbloom.co.nz number 0218463307 and the instagram logo
- The benefits of spending money of the look and feel of gardens to maximize there chance of quick and profitable sale. wow factor and so on. Free estimate no obligation
Nice to have
- Any thing you can add to the layout that would help as sound professional and get our point across.

```html
<!DOCTYPE html>
<html lang="en">
<head>
<meta charset="utf-8">
<title>Trvbloom Landscaping – Presale Garden Postcard</title>
<link href="https://fonts.googleapis.com/css2?family=Montserrat:wght@500;700;800&family=Lato:wght@400;700&display=swap" rel="stylesheet">
<style>
  :root {
    --page: #e6e7e9;
    --white: #ffffff;
    --green: #9ad91f;
    --green-light: #a6e32a;
    --blue: #1160b8;
    --blue-deep: #0b4fa3;
    --ink: #1e2a1a;
    --black: #111111;
    --sky: #8fb3d9;
    --house: #e9e2cf;
    --lawn: #6f9a3c;
  }
  * { margin: 0; padding: 0; box-sizing: border-box; }
  html, body { width: 1200px; height: 848px; overflow: hidden; background: var(--page); }
  .postcard {
    position: absolute; left: 0; top: 24px;
    width: 1200px; height: 800px;
    background: var(--white);
    overflow: hidden;
    font-family: "Montserrat", sans-serif;
  }
  .hero-photo {
    position: absolute; left: 495px; top: 0; width: 705px; height: 632px;
    background: linear-gradient(180deg, var(--white) 0%, var(--sky) 22%, var(--house) 48%, #d9d3c3 70%, var(--lawn) 100%);
  }
  .brand-panel {
    position: absolute; left: 0; top: 139px; width: 495px; height: 557px;
    background: linear-gradient(180deg, var(--green-light), var(--green));
  }
  .brand-name {
    position: absolute; left: 0; top: 30px; width: 495px;
    display: flex; flex-direction: column; align-items: center;
  }
  .brand-name span {
    font-weight: 800; color: var(--black); font-size: 34px; line-height: 38px; letter-spacing: 1px;
  }
  .brand-name span.sub { font-size: 16px; line-height: 20px; letter-spacing: 4px; }
  .tagline {
    position: absolute; left: 0; top: 176px; width: 495px;
    text-align: center; color: var(--white);
    font-weight: 500; font-size: 30px; line-height: 38px;
  }
  .benefit {
    position: absolute; left: 40px; top: 258px; width: 415px;
    text-align: center; color: var(--ink);
    font-family: "Lato", sans-serif; font-weight: 700; font-size: 23px; line-height: 30px;
  }
  .estimate-box {
    position: absolute; left: 0; top: 397px; width: 460px; height: 136px;
    background: var(--blue); border-radius: 0 22px 22px 0;
    color: var(--white); font-weight: 800; padding-left: 43px;
  }
  .estimate-box .line1 { display: block; font-size: 38px; line-height: 44px; margin-top: 16px; white-space: nowrap; }
  .estimate-box .line2 { display: block; font-size: 46px; line-height: 56px; margin-top: 10px; white-space: nowrap; }
  .social-bar {
    position: absolute; left: 0; top: 720px; width: 495px; height: 51px;
    background: var(--blue);
    display: flex; align-items: center; justify-content: flex-end; padding-right: 32px; gap: 14px;
    color: var(--white); font-weight: 500; font-size: 26px;
  }
  .social-bar svg { width: 34px; height: 34px; }
  .contact-band { position: absolute; left: 495px; top: 632px; width: 705px; height: 168px; }
  .contact-band svg { position: absolute; left: 0; top: 0; }
  .call-line {
    position: absolute; left: 85px; top: 34px;
    color: var(--white); font-weight: 800; font-size: 49px; line-height: 56px; white-space: nowrap;
  }
  .email-line {
    position: absolute; left: 85px; top: 97px;
    color: var(--white); font-weight: 500; font-size: 28px; line-height: 34px; white-space: nowrap;
  }
  .contact-rule {
    position: absolute; left: 79px; top: 138px; width: 578px; height: 4px; background: var(--green);
  }
</style>
</head>
<body>
  <main class="postcard">
    <div class="hero-photo" role="img" aria-label="Photo of a smiling mature couple standing in front of a two-storey house with a Home For Sale sign on the lawn"></div>

    <section class="brand-panel">
      <div class="brand-name"><span>TRVBLOOM</span><span class="sub">LANDSCAPING</span></div>
      <h1 class="tagline">A landscaping and premium garden maintenance company</h1>
      <p class="benefit">The benefits of spending money of the look and feel of gardens to maximize there chance of quick and profitable sale.</p>
      <div class="estimate-box">
        <span class="line1">FREE ESTIMATE</span>
        <span class="line2">No obligation</span>
      </div>
    </section>

    <div class="social-bar">
      <svg viewBox="0 0 34 34" aria-hidden="true">
        <circle cx="17" cy="17" r="14" fill="none" stroke="#ffffff" stroke-width="3"/>
      </svg>
      <span>trvbloom_landscaping</span>
    </div>

    <section class="contact-band">
      <svg width="705" height="168" viewBox="0 0 705 168" aria-hidden="true">
        <polygon points="0,0 67,0 0,63" fill="#7fbf1e"/>
        <polygon points="67,0 705,0 705,168 0,168 0,63" fill="#1160b8"/>
      </svg>
      <div class="call-line">CALL US : 0218463307</div>
      <div class="email-line">Email address neil@trvbloom.co.nz</div>
      <div class="contact-rule"></div>
    </section>
  </main>
</body>
</html>
```